Landing Page IT Security Vendor

We need a landing page that uses our colour scheme (www.veldonguard.com). We created a draft (see attached). We do not need standard stock template design pages. Please only apply if you can design pages from scratch and try to be as close as possible to our draft. It is ok to also purchase commecrial stock pictures

Coding

Coded - Design and coding required

Number of Pages Required

1 page

```html
<!DOCTYPE html>
<html lang="en">
<head>
<meta charset="utf-8">
<title>Veldon Guard – Security Awareness</title>
<link href="https://fonts.googleapis.com/css2?family=Montserrat:wght@400;600;700;800&family=Open+Sans:wght@400;600&display=swap" rel="stylesheet">
<style>
:root{
  --teal:#2fb3b6;
  --teal-dark:#1f9a9e;
  --teal-deep:#168a8e;
  --orange:#f39a1e;
  --ink:#333b40;
  --grey:#8a9297;
  --band:#9aa1a5;
  --white:#ffffff;
  --light:#f2f4f5;
}
*{box-sizing:border-box;margin:0;padding:0}
html,body{width:686px;height:1200px;overflow:hidden}
body{font-family:"Open Sans",Arial,sans-serif;color:var(--ink);background:var(--white);position:relative}
.topbar{position:absolute;top:0;left:0;width:686px;height:40px;background:var(--white);display:flex;align-items:center;padding:0 14px}
.brand{font-family:"Montserrat",sans-serif;font-weight:800;font-size:16px;color:var(--orange);display:flex;align-items:center;gap:6px;width:150px}
.brand-dot{width:12px;height:12px;background:var(--orange);border-radius:50%}
.features{display:flex;gap:18px;flex:1}
.feature{display:flex;align-items:flex-start;gap:5px;font-size:6px;line-height:8px;color:var(--grey);width:150px}
.feature svg{flex:none}
.hero{position:absolute;top:40px;left:0;width:686px;height:500px;background:var(--teal);overflow:hidden}
.hero-photo{position:absolute;right:0;top:0;width:330px;height:300px;background:linear-gradient(120deg,rgba(47,179,182,0) 0%,#7fcfcf 35%,#d9a58c 70%,#b45a4a 100%)}
.nav{position:absolute;top:10px;left:60px;display:flex;gap:6px}
.nav span{font-size:8px;padding:4px 12px;border-radius:12px;color:var(--white);background:var(--teal-dark)}
.nav span.active{background:var(--white);color:var(--teal-deep)}
.demo-btn{position:absolute;top:24px;right:190px;font-size:8px;color:var(--white);border:1px solid var(--white);border-radius:3px;padding:4px 10px;background:var(--teal-deep)}
.kicker{position:absolute;top:60px;left:60px;font-family:"Montserrat",sans-serif;font-size:13px;color:var(--white);letter-spacing:.5px}
.headline{position:absolute;top:98px;left:60px;width:440px;font-family:"Montserrat",sans-serif;font-weight:800;font-size:27px;line-height:31px;color:var(--white);text-transform:uppercase}
.cards{position:absolute;top:280px;left:60px;display:flex;gap:16px}
.card{width:178px;height:205px;background:var(--white);border-top:3px solid var(--orange);padding:12px 10px;box-shadow:0 2px 6px rgba(0,0,0,.15);position:relative}
.card h3{font-family:"Montserrat",sans-serif;font-weight:700;font-size:10px;line-height:12px;color:var(--orange);text-transform:uppercase;margin-bottom:8px}
.card p{font-size:6.5px;line-height:9px;color:var(--ink);margin-bottom:5px}
.card .btn{position:absolute;left:10px;bottom:14px;font-size:6.5px;font-weight:600;color:var(--white);background:var(--orange);padding:5px 12px;text-transform:uppercase}
.msp-band{position:absolute;top:548px;left:0;width:686px;height:38px;background:var(--band);color:var(--white);font-size:9px;display:flex;align-items:center;justify-content:center;gap:4px}
.msp-band u{font-weight:600}
.trust{position:absolute;top:600px;left:0;width:686px;height:390px;background:var(--white)}
.trust-copy{position:absolute;left:40px;top:28px;width:330px}
.trust-copy h2{font-family:"Montserrat",sans-serif;font-weight:600;font-size:16px;line-height:21px;color:var(--ink);margin-bottom:16px}
.trust-copy h2 .num{color:var(--orange)}
.trust-copy p{font-size:9px;line-height:14px;color:var(--ink);margin-bottom:14px}
.partners{position:absolute;left:410px;top:40px;display:grid;grid-template-columns:repeat(3,72px);gap:12px 10px}
.partner{height:30px;border-radius:3px}
.p1{background:#1e3f8a}.p2{background:#d8232a}.p3{background:#e2001a}.p4{background:#8c8c8c}.p5{background:#2c6fb3}.p6{background:#5a6b78}
.p7{background:#1e4e8f}.p8{background:#b5b5b5}.p9{background:#3d3d3d}
.footer{position:absolute;top:995px;left:0;width:686px;height:150px;background:var(--teal-dark);color:var(--white);padding:22px 40px;display:flex;gap:34px}
.footer h4{font-family:"Montserrat",sans-serif;font-size:9px;font-weight:700;margin-bottom:8px;letter-spacing:.5px}
.footer p{font-size:6.5px;line-height:10px;opacity:.92}
.col{width:120px}
.lang{margin-left:auto;width:110px}
.lang .select{margin-top:4px;font-size:7px;border-bottom:1px solid rgba(255,255,255,.6);padding-bottom:3px}
.badges{position:absolute;top:1145px;left:0;width:686px;height:55px;background:var(--white);display:flex;align-items:center;justify-content:center;gap:18px}
.badge{width:30px;height:30px;border-radius:50%;background:var(--light);border:2px solid #d4a53a}
.badge.sq{border-radius:4px;border-color:var(--teal)}
</style>
</head>
<body>
<header class="topbar">
  <div class="brand"><span class="brand-dot"></span>VELDON</div>
  <div class="features">
    <div class="feature"><svg width="10" height="10" viewBox="0 0 10 10"><circle cx="5" cy="5" r="4" fill="none" stroke="#2fb3b6"/><path d="M3 5l1.5 1.5L7 4" stroke="#2fb3b6" fill="none"/></svg><span>Trusted by global firms in more than forty nations</span></div>
    <div class="feature"><svg width="10" height="10" viewBox="0 0 10 10"><circle cx="5" cy="5" r="4" fill="none" stroke="#2fb3b6"/><path d="M3 5l1.5 1.5L7 4" stroke="#2fb3b6" fill="none"/></svg><span>Awarded leading training platform three years running</span></div>
    <div class="feature"><svg width="10" height="10" viewBox="0 0 10 10"><circle cx="5" cy="5" r="4" fill="none" stroke="#2fb3b6"/><path d="M3 5l1.5 1.5L7 4" stroke="#2fb3b6" fill="none"/></svg><span>Over three hundred ready modules in many languages</span></div>
  </div>
</header>

<section class="hero">
  <div class="hero-photo" role="img" aria-label="Photo of a woman holding a tablet in an office setting"></div>
  <nav class="nav"><span class="active">Home</span><span>Solution ▾</span></nav>
  <div class="demo-btn">Request a demo</div>
  <p class="kicker">CYBER SECURITY STARTS WITH PEOPLE</p>
  <h1 class="headline">Train your staff with Veldon and improve cyber security awarness</h1>
  <div class="cards">
    <article class="card">
      <h3>Import our training courses in your LMS</h3>
      <p>Buy out-of-the-box or custom tailored security courses you can import to your elearning system.</p>
      <p>Veldon offers 250 fully customizable training modules in 30 languages: games, videos, quizzes, posters, offline micro-training and much more.</p>
      <span class="btn">Explore our training</span>
    </article>
    <article class="card">
      <h3>Let us develop a security awareness program</h3>
      <p>Veldon Guard will assist you in improving security awareness with money back guarantee.</p>
      <p>Our security awareness specialists will identify risks using simulations. We develop a tailored awareness program and reduce your exposure to social hacking.</p>
      <span class="btn">Explore our services</span>
    </article>
    <article class="card">
      <h3>Install the Veldon software on premise or get access to the SaaS version</h3>
      <p>You want to run the campaigns yourself? Choose your preferred setup type and get started.</p>
      <p>The software can be installed on premise or in the cloud. If you don't want to deal with the installation, we onboard you in the cloud.</p>
      <span class="btn">Explore our software</span>
    </article>
  </div>
</section>

<div class="msp-band">Veldon is also available for MSSP – <u>Learn more</u></div>

<section class="trust">
  <div class="trust-copy">
    <h2>Already over <span class="num">12000000</span><br>Employees worldwide trust and use Veldon.</h2>
    <p>Veldon Guard is a name you can trust! Because we won countless awards since 2015, and help well-known brands around the world.</p>
    <p>You know you're getting a quality solution with us.</p>
    <p>Our services can be customized to fit your needs and company size. Talk to our team today to learn more.</p>
  </div>
  <div class="partners" role="img" aria-label="Partner company logos">
    <div class="partner p1"></div><div class="partner p2"></div><div class="partner p3"></div>
    <div class="partner p4"></div><div class="partner p5"></div><div class="partner p6"></div>
    <div class="partner p7"></div><div class="partner p8"></div><div class="partner p9"></div>
  </div>
</section>

<footer class="footer">
  <div class="col">
    <h4>CONTACTS</h4>
    <p>Veldon Guard AG<br>Weststrasse 14<br>8000 Sample City<br>www.veldonguard.com</p>
  </div>
  <div class="col">
    <h4>&nbsp;</h4>
    <p>Veldon Guard Inc.<br>120 Harbor Lane<br>Suite 400<br>Austin, TX 70000</p>
  </div>
  <div class="col">
    <h4>&nbsp;</h4>
    <p>Phone Main +00 00 000 0000<br>Phone US +0 000 000 0000<br>Phone Support +00 00 000 0001<br>Phone Sales +00 00 000 0002</p>
  </div>
  <div class="lang">
    <h4>LANGUAGE</h4>
    <div class="select">English ▾</div>
  </div>
</footer>

<div class="badges" role="img" aria-label="Award and certification badges">
  <div class="badge"></div><div class="badge"></div><div class="badge sq"></div><div class="badge"></div><div class="badge sq"></div><div class="badge"></div><div class="badge"></div><div class="badge sq"></div>
</div>
</body>
</html>
```